Ashby Meadows Thank-You Tag

Looking for a file that incorporates current branding/colors and says:

"Thanks for Swimming with Us!"
Ashby Meadows Otters

Samples of other pieces we've done recently are attached.

Will be printed on cardstock that is
Width: 3.5 inches
Height: 2.5 inches

```html
<!DOCTYPE html>
<html lang="en">
<head>
<meta charset="utf-8">
<title>Ashby Meadows Otters Thank-You Tag</title>
<link href="https://fonts.googleapis.com/css2?family=Playball&family=Montserrat:wght@700;800&family=Graduate&display=swap" rel="stylesheet">
<style>
  :root {
    --pool-blue: #2750a9;
    --bubble-pink: #f262a2;
    --sky-blue: #9fc6ea;
    --white: #ffffff;
    --backdrop: #e9e9ec;
    --dolphin-light: #cfe4f4;
    --dolphin-dark: #3b87c4;
  }
  html, body {
    margin: 0;
    width: 1200px;
    height: 900px;
    overflow: hidden;
    background: var(--backdrop);
  }
  .tag {
    position: absolute;
    left: 75px;
    top: 75px;
    width: 1050px;
    height: 750px;
    background: var(--pool-blue);
    overflow: hidden;
    box-shadow: 0 6px 20px rgba(0,0,0,0.18);
  }
  .tag-art {
    position: absolute;
    inset: 0;
  }
  .thanks-message {
    position: absolute;
    left: 50px;
    top: 150px;
    width: 470px;
    margin: 0;
    font-family: "Playball", cursive;
    font-weight: 400;
    font-size: 86px;
    line-height: 1;
    color: var(--white);
    text-align: center;
  }
  .season-year {
    position: absolute;
    left: 640px;
    top: 0;
    width: 400px;
    height: 400px;
    font-family: "Montserrat", sans-serif;
    font-weight: 800;
    line-height: 1;
  }
  .year-two {
    position: absolute;
    left: 0;
    top: 10px;
    font-size: 200px;
    color: var(--white);
  }
  .year-zero-mark {
    position: absolute;
    left: 150px;
    top: 48px;
    width: 150px;
    height: 150px;
    border-radius: 50%;
    background: var(--white);
    display: flex;
    align-items: center;
    justify-content: center;
  }
  .year-zero-mark span {
    font-family: "Montserrat", sans-serif;
    font-weight: 700;
    font-size: 19px;
    line-height: 1.15;
    color: var(--pool-blue);
    text-align: center;
  }
  .year-twenty-six {
    position: absolute;
    left: 110px;
    top: 160px;
    font-size: 200px;
    color: var(--bubble-pink);
    letter-spacing: -6px;
  }
  .team-name {
    position: absolute;
    left: 330px;
    top: 676px;
    margin: 0;
    font-family: "Graduate", serif;
    font-weight: 400;
    font-size: 44px;
    line-height: 48px;
    letter-spacing: 1px;
    color: var(--white);
    white-space: nowrap;
    transform: rotate(-14deg);
    transform-origin: left center;
  }
  .dolphin {
    position: absolute;
    border-radius: 55% 45% 50% 50% / 60% 60% 40% 40%;
    background: linear-gradient(160deg, var(--dolphin-light), var(--dolphin-dark));
  }
  .dolphin-small {
    left: 190px;
    top: 440px;
    width: 120px;
    height: 280px;
    transform: rotate(-15deg);
  }
  .dolphin-large {
    left: 470px;
    top: 250px;
    width: 160px;
    height: 310px;
    transform: rotate(-20deg);
  }
  .splash {
    position: absolute;
    left: 690px;
    top: 390px;
    width: 55px;
    height: 48px;
    border-radius: 50% 50% 40% 40%;
    background: var(--sky-blue);
    opacity: 0.8;
  }
</style>
</head>
<body>
  <div class="tag">
    <svg class="tag-art" width="1050" height="750" viewBox="0 0 1050 750" aria-hidden="true">
      <circle class="pink-bubble" cx="230" cy="190" r="400" fill="var(--bubble-pink)"/>
      <path class="wave-body" d="M0,690 C250,670 420,610 580,540 S860,450 1050,440 L1050,750 L0,750 Z" fill="var(--pool-blue)"/>
      <path class="wave-sky" d="M0,650 C250,630 420,570 580,500 S860,410 1050,400" fill="none" stroke="var(--sky-blue)" stroke-width="34"/>
      <path class="wave-white" d="M0,672 C250,652 420,592 580,522 S860,432 1050,422" fill="none" stroke="var(--white)" stroke-width="12"/>
      <path class="wave-pink" d="M0,690 C250,670 420,610 580,540 S860,450 1050,440" fill="none" stroke="var(--bubble-pink)" stroke-width="26"/>
    </svg>

    <p class="thanks-message">Thanks for<br>Swimming<br>with Us!</p>

    <div class="season-year" aria-label="2026">
      <span class="year-two">2</span>
      <div class="year-zero-mark"><span>ASHBY<br>MEADOWS</span></div>
      <span class="year-twenty-six">26</span>
    </div>

    <div class="dolphin dolphin-small" role="img" aria-label="Illustration of a small leaping dolphin"></div>
    <div class="dolphin dolphin-large" role="img" aria-label="Illustration of a large leaping dolphin"></div>
    <div class="splash" role="img" aria-label="Small water splash decoration"></div>

    <p class="team-name">ASHBY MEADOWS OTTERS</p>
  </div>
</body>
</html>
```